Billboard design for a small town Oral Surgeon

We are getting several billboards and need a design that highlights the doctors photo, and bullet points of what he does. Our business name is extremely long, so it’s a challenge to figure out how to do this. Maybe just use our logo? Open to ideas.
The logo can be shortened as designer sees fit, meaning we can drop the tag line. Important info to include:
Doctors name is Lorvik Tamsen
The highlighted bullet points are:
•Implants
•wisdom teeth
•Jaw Surgery
•facial trauma
The goal of this billboard is to let our community know that they have an option here in Ada, our town. Many still drive to the city a couple hours away not knowing they now have an option here at home. Having a hard time finding examples of what I have in mind, so hoping this will get us going. I want it as “non-busy” as possible, so no unnecessary lines or anything that competes with the information we are trying to get across.

Target Market(s)

Everyone in town, just trying to spread the word that we are here

Industry/Entity Type

Medical/surgical (oral surgery)

Font styles to use
Sans Serif

Colors
0094D4
00A9DD
6FCCEA
C7EBF8
E9F6FB

Requirements
Must have
• *New note** Due to location of billboard, I prefer the photo of doctor to be on the left side. Must look neat and professional. Must highlight what we do.
Nice to have
• Our colors are a blue-green with silver, against black or white, but I’m flexible on this, I don’t necessarily need the colors highlighted. I’m also flexible on font style, just needs to be easy to read.
Should not have
• Distracting graphics, should not look like a dental office. That’s an issue we have is people thinking we are another dental office, we do not do any general dentistry, it’s surgery only.

```html
<!DOCTYPE html>
<html lang="en">
<head>
<meta charset="utf-8">
<title>Redbud Valley Oral &amp; Maxillofacial Surgery – Billboard</title>
<link href="https://fonts.googleapis.com/css2?family=Oswald:wght@500;700&family=Poppins:wght@600;700&family=Raleway:wght@400&display=swap" rel="stylesheet">
<style>
  :root {
    --page: #e4e4e6;
    --board: #16161a;
    --silver: #e8e8ea;
    --silver-dark: #b9babd;
    --teal: #0d93b3;
    --green: #3c8074;
    --ink: #111114;
    --white: #ffffff;
  }
  * { margin: 0; padding: 0; box-sizing: border-box; }
  html, body { width: 915px; height: 1200px; overflow: hidden; background: var(--page); }
  .billboard {
    position: absolute; left: 20px; top: 454px;
    width: 875px; height: 292px;
    background: var(--board);
    overflow: hidden;
    box-shadow: 0 6px 14px rgba(0,0,0,.35);
  }
  .doctor-photo {
    position: absolute; left: 0; top: 0; width: 265px; height: 292px;
    background: linear-gradient(180deg, #3a3b44 0%, #8a6b5c 40%, #262a3a 75%, #1b1e2b 100%);
  }
  .name-band {
    position: absolute; left: 0; bottom: 0; width: 480px; height: 62px;
  }
  .doctor-name {
    position: absolute; right: 407px; bottom: 17px;
    font: 700 22px "Poppins", sans-serif; color: var(--white); white-space: nowrap;
  }
  .practice {
    position: absolute; left: 220px; top: 28px; width: 230px;
    font-family: "Raleway", sans-serif; color: var(--silver);
  }
  .practice-mark {
    width: 96px; height: 96px; margin: 0 0 20px 72px;
    border: 3px solid var(--silver-dark); border-radius: 50%;
  }
  .practice-name {
    font-size: 14.5px; line-height: 19px; letter-spacing: -0.2px;
    white-space: nowrap;
  }
  .practice-rule { height: 1px; background: var(--silver-dark); margin: 3px 0 4px; }
  .practice-tagline { font-size: 8.5px; letter-spacing: 2.6px; white-space: nowrap; }
  .headline {
    position: absolute; left: 476px; top: 14px; width: 374px;
    font: 700 38px/50px "Oswald", sans-serif; color: var(--silver);
    letter-spacing: .3px; text-align: right; white-space: nowrap;
  }
  .services {
    position: absolute; left: 481px; top: 81px; width: 369px;
    display: grid; grid-template-columns: 1fr 1fr; gap: 6px 5px;
  }
  .service {
    height: 38px; display: flex; align-items: center; justify-content: center;
    font: 500 21px "Oswald", sans-serif; color: var(--white); letter-spacing: .3px;
  }
  .service--green { background: var(--green); }
  .service--blue { background: var(--teal); }
  .booking {
    position: absolute; left: 481px; top: 180px; width: 369px;
    display: flex; align-items: center; justify-content: space-between;
  }
  .booking-label { font: 500 24px "Oswald", sans-serif; color: var(--teal); }
  .booking-icon { width: 24px; height: 24px; margin: 0 6px 0 4px; }
  .booking-phone { font: 700 23px "Poppins", sans-serif; color: var(--white); }
  .booking-group { display: flex; align-items: center; }
  .address-bar {
    position: absolute; left: 480px; bottom: 0; width: 395px; height: 62px;
    background: var(--white); display: flex; align-items: center; padding-left: 12px;
  }
  .address-pin { width: 16px; height: 18px; margin-right: 6px; }
  .address { font: 600 14px "Poppins", sans-serif; color: var(--ink); white-space: nowrap; }
</style>
</head>
<body>
  <div class="billboard">
    <div class="doctor-photo" role="img" aria-label="Portrait photo of the surgeon in a dark suit and red tie"></div>

    <svg class="name-band" viewBox="0 0 480 62" aria-hidden="true">
      <polygon points="215,0 480,0 480,62 258,62" fill="var(--teal)"/>
    </svg>
    <div class="doctor-name">Lorvik Tamsen, D.D.S.</div>

    <div class="practice">
      <div class="practice-mark"></div>
      <div class="practice-name">REDBUD VALLEY ORAL<br>&amp; MAXILLOFACIAL SURGERY</div>
      <div class="practice-rule"></div>
      <div class="practice-tagline">COMFORT|CARE|COMPASSION</div>
    </div>

    <h1 class="headline">THE NEW LOCALE IN ADA</h1>

    <div class="services">
      <div class="service service--green">JAW SURGERY</div>
      <div class="service service--blue">FACIAL TRAUMA</div>
      <div class="service service--blue">IMPLANTS</div>
      <div class="service service--green">WISDOM TEETH</div>
    </div>

    <div class="booking">
      <div class="booking-group">
        <span class="booking-label">BOOK TODAY</span>
        <svg class="booking-icon" viewBox="0 0 24 24" aria-hidden="true">
          <circle cx="12" cy="12" r="11" fill="var(--green)"/>
          <path d="M8.2 6.5l2 2.3-1.1 1.6c.8 1.7 2 2.9 3.7 3.7l1.6-1.1 2.3 2-1.3 2c-4.6-.4-8.4-4.2-8.8-8.8z" fill="var(--board)"/>
        </svg>
      </div>
      <span class="booking-phone">(580) 555-0142</span>
    </div>

    <div class="address-bar">
      <svg class="address-pin" viewBox="0 0 16 18" aria-hidden="true">
        <path d="M8 1a5 5 0 0 0-5 5c0 3.6 5 8 5 8s5-4.4 5-8a5 5 0 0 0-5-5z" fill="none" stroke="var(--green)" stroke-width="2"/>
        <circle cx="8" cy="6" r="1.8" fill="var(--green)"/>
        <path d="M2 16h12" stroke="var(--green)" stroke-width="2"/>
      </svg>
      <span class="address">412 N Cedar Ridge St. Ada, OK 74820, USA</span>
    </div>
  </div>
</body>
</html>
```